Meridian Callware business card design

I would like to see some designs for a business card for Meridian Callware. I would like the business card to be double sided. It will need to have a similar colour / look and feel to our website www.meridiancallware.com.au I have also attached our latest flyer. Final designs to be handed over in Photoshop format so that I can edit the business card when needed please.

Industry/Entity Type

Business

Contact Information for Business Card

Kelvin Ashworth
sales@meridiancallware.com.au
Business Development Manager
ph: (08) 6517 2984
www.meridiancallware.com.au

Font styles to use
Serif
Sans Serif

Requirements
Must have
• If you could please utilise our colour scheme as seen on our website and the attached flyer.
• I would also like the final design to be in a Photoshop format so that I can edit it when needed please.

```html
<!DOCTYPE html>
<html lang="en">
<head>
<meta charset="utf-8">
<title>Meridian Callware – Business Card</title>
<link rel="stylesheet" href="https://fonts.googleapis.com/css2?family=Open+Sans:ital,wght@0,400;0,600;0,700;1,700&display=swap">
<style>
  :root {
    --bg: #ece9e4;
    --brand-blue: #1b82c2;
    --brand-blue-dark: #0f6aa6;
    --brand-blue-light: #3aa2dc;
    --ink: #3a3a3a;
    --ink-soft: #4a4a4a;
    --band-dark: #2d2d2d;
    --card-white: #ffffff;
    --card-grey: #e4e4e4;
  }
  * { margin: 0; padding: 0; box-sizing: border-box; }
  html, body { width: 1200px; height: 843px; overflow: hidden; }
  body {
    background: var(--bg);
    font-family: "Open Sans", Arial, sans-serif;
    display: flex;
    align-items: center;
    justify-content: center;
    gap: 40px;
  }
  .card {
    position: relative;
    width: 540px;
    height: 310px;
    border-radius: 18px;
    overflow: hidden;
    box-shadow: 0 10px 30px rgba(0,0,0,.18);
  }

  /* Back side */
  .card--back {
    background: linear-gradient(135deg, var(--brand-blue-light) 0%, var(--brand-blue) 50%, var(--brand-blue-dark) 100%);
    display: flex;
    align-items: center;
    justify-content: center;
  }
  .card--back .wordmark {
    color: var(--card-white);
    font-size: 40px;
    font-weight: 600;
    letter-spacing: -0.5px;
  }

  /* Front side */
  .card--front {
    background: linear-gradient(120deg, var(--card-white) 35%, var(--card-grey) 100%);
  }
  .card--front .wordmark {
    position: absolute;
    left: 30px;
    top: 108px;
    color: var(--ink-soft);
    font-size: 25px;
    font-weight: 600;
    letter-spacing: -0.4px;
  }
  .contact {
    position: absolute;
    left: 300px;
    top: 102px;
    color: var(--ink);
    font-size: 13px;
    line-height: 1.45;
  }
  .contact__name {
    color: var(--brand-blue);
    font-size: 20px;
    font-weight: 700;
    line-height: 1.2;
  }
  .contact__role { font-size: 13.5px; margin-bottom: 4px; }
  .contact__label { color: var(--brand-blue); font-weight: 700; font-style: italic; }

  .footer-bands {
    position: absolute;
    left: 0;
    bottom: 0;
    width: 540px;
    height: 90px;
  }
  .website {
    position: absolute;
    left: 60px;
    bottom: 52px;
    color: var(--card-white);
    font-size: 13px;
    letter-spacing: 1.5px;
  }
</style>
</head>
<body>

  <section class="card card--back" aria-label="Card back">
    <span class="wordmark">Meridian Callware</span>
  </section>

  <section class="card card--front" aria-label="Card front">
    <span class="wordmark">Meridian Callware</span>

    <div class="contact">
      <div class="contact__name">Kelvin Ashworth</div>
      <div class="contact__role">Business Development Manager</div>
      <div><span class="contact__label">Phone:</span> (08) 6517 2984</div>
      <div>sales@meridiancallware.com.au</div>
    </div>

    <svg class="footer-bands" viewBox="0 0 540 90" aria-hidden="true">
      <defs>
        <linearGradient id="blueBand" x1="0" x2="1" y1="0" y2="0">
          <stop offset="0" stop-color="#3aa2dc"/>
          <stop offset="1" stop-color="#1b82c2"/>
        </linearGradient>
      </defs>
      <polygon points="0,12 380,12 400,46 0,46" fill="url(#blueBand)"/>
      <polygon points="0,46 400,46 404,52 0,52" fill="#9fcbe6"/>
      <polygon points="382,46 540,46 540,70 396,70" fill="#2d2d2d"/>
      <circle cx="392" cy="40" r="13" fill="#ffffff" stroke="#1b82c2" stroke-width="3"/>
    </svg>
    <span class="website">www.meridiancallware.com.au</span>
  </section>

</body>
</html>
```